Fish guide business card

Buisiness card

Target Market(s)

Visitors to Campbell River Bc wanting to catch fish in the ocean and have a memorable adventure fun filled day

Industry/Entity Type

Tourism

Contact Information for Business Card

Phone number 250 318 two cards Ray 250 318 7262 other card Lou 250 6093714 both have email info@lwgullrocktours.com and website www.lwgullrocktours.com

Requirements
Must have
• Email, website , name , phone , logo , Campbell River BC
Nice to have
• Uploaded pictures have boat and man with fish picture

```html
<!DOCTYPE html>
<html lang="en">
<head>
<meta charset="utf-8">
<title>LW Gull Rock Tours – Business Card</title>
<link href="https://fonts.googleapis.com/css2?family=Arimo:wght@400;700&display=swap" rel="stylesheet">
<style>
  :root {
    --bg: #c9c9cb;
    --paper: #ffffff;
    --navy: #34327a;
    --navy-deep: #2a2870;
    --navy-light: #4a48a0;
    --ink-soft: #5a5890;
    --photo-sea: #7d8fa6;
    --photo-grey: #c8ccd4;
    --ghost: #e4e5ea;
  }
  * { box-sizing: border-box; margin: 0; padding: 0; }
  html, body {
    width: 1200px; height: 876px; overflow: hidden;
    background: var(--bg);
    font-family: "Arimo", Arial, sans-serif;
  }
  .stage {
    position: relative; width: 1200px; height: 876px;
    display: flex; justify-content: center; align-items: center; gap: 110px;
  }
  .card {
    position: relative; width: 340px; height: 590px;
    border-radius: 24px; overflow: hidden;
    box-shadow: 0 6px 18px rgba(0,0,0,0.18);
  }

  /* Shared brand lockup */
  .brand-mark {
    position: absolute; left: 0; right: 0; top: 140px;
    display: flex; flex-direction: column; align-items: center; gap: 12px;
  }
  .brand-mark .ring {
    width: 120px; height: 120px; border-radius: 50%;
    border: 5px solid var(--navy);
  }
  .brand-mark .name {
    font-weight: 700; font-size: 19px; color: var(--navy);
    letter-spacing: 0.5px; white-space: nowrap; text-align: center;
  }

  /* Front: contact side */
  .card--front { background: var(--paper); }
  .card--front .ghost-photo {
    position: absolute; left: 0; top: 0; width: 190px; height: 370px;
    background: radial-gradient(ellipse at 45% 45%, var(--ghost) 0%, rgba(228,229,234,0.5) 55%, rgba(255,255,255,0) 80%);
  }
  .contact {
    position: absolute; left: 30px; right: 20px; top: 340px;
    display: flex; align-items: flex-start;
  }
  .contact .person {
    font-weight: 700; font-size: 22px; color: var(--navy-light);
    padding-right: 14px; padding-top: 4px;
  }
  .contact .divider {
    width: 1.5px; height: 100px; background: var(--navy-light); margin-right: 12px; flex: none;
  }
  .contact ul { list-style: none; display: flex; flex-direction: column; gap: 9px; }
  .contact li {
    display: flex; align-items: center; gap: 8px;
    font-size: 16px; color: var(--ink-soft); white-space: nowrap;
  }
  .contact svg { width: 14px; height: 14px; fill: var(--navy); flex: none; }

  /* Back: photo side */
  .card--back {
    background: linear-gradient(160deg, var(--navy-light) 0%, var(--navy) 50%, var(--navy-deep) 100%);
  }
  .card--back .boat-photo {
    position: absolute; left: 0; top: 0; width: 260px; height: 340px;
    background: linear-gradient(170deg, var(--photo-grey) 0%, var(--photo-sea) 55%, rgba(74,72,160,0) 100%);
    -webkit-mask-image: linear-gradient(to right, #000 55%, transparent 100%);
    mask-image: linear-gradient(to right, #000 55%, transparent 100%);
    opacity: 0.85;
  }
  .card--back .angler-photo {
    position: absolute; left: 40px; bottom: 0; width: 300px; height: 230px;
    background: linear-gradient(180deg, rgba(200,204,212,0) 0%, #8f96a3 40%, #3c4a3a 100%);
    border-radius: 60px 0 0 0;
    opacity: 0.9;
  }
  .card--back .brand-mark { top: 110px; }
  .card--back .brand-mark .ring { border-color: var(--paper); }
  .card--back .brand-mark .name { color: var(--paper); }
</style>
</head>
<body>
<main class="stage">
  <section class="card card--front">
    <div class="ghost-photo" role="img" aria-label="Faded photo of an angler holding a large salmon"></div>
    <div class="brand-mark">
      <div class="ring"></div>
      <div class="name">LW Gull Rock Tours</div>
    </div>
    <div class="contact">
      <div class="person">RAY</div>
      <div class="divider"></div>
      <ul>
        <li>
          <svg viewBox="0 0 24 24"><path d="M6.6 10.8a15 15 0 0 0 6.6 6.6l2.2-2.2a1 1 0 0 1 1-.25 11.4 11.4 0 0 0 3.6.57 1 1 0 0 1 1 1V20a1 1 0 0 1-1 1A17 17 0 0 1 3 4a1 1 0 0 1 1-1h3.5a1 1 0 0 1 1 1c0 1.25.2 2.45.57 3.6a1 1 0 0 1-.25 1z"/></svg>
          250 318 7262
        </li>
        <li>
          <svg viewBox="0 0 24 24"><path d="M2 5h20v14H2z M4 7v.5l8 5.5 8-5.5V7z" fill-rule="evenodd"/></svg>
          info@lwgullrocktours.com
        </li>
        <li>
          <svg viewBox="0 0 24 24"><circle cx="12" cy="12" r="10"/><path d="M2 12h20M12 2c3 3 3 17 0 20M12 2c-3 3-3 17 0 20" stroke="#fff" stroke-width="1.5" fill="none"/></svg>
          www.lwgullrocktours.com
        </li>
        <li>
          <svg viewBox="0 0 24 24"><path d="M12 2a7 7 0 0 0-7 7c0 5 7 13 7 13s7-8 7-13a7 7 0 0 0-7-7zm0 9.5A2.5 2.5 0 1 1 12 6.5a2.5 2.5 0 0 1 0 5z"/></svg>
          Campbell River BC
        </li>
      </ul>
    </div>
  </section>

  <section class="card card--back">
    <div class="boat-photo" role="img" aria-label="Photo of a white fishing boat moored at a dock"></div>
    <div class="angler-photo" role="img" aria-label="Photo of a guide in a cap holding a large salmon"></div>
    <div class="brand-mark">
      <div class="ring"></div>
      <div class="name">LW Gull Rock Tours</div>
    </div>
  </section>
</main>
</body>
</html>
```